Business Cards

Brookvale Property Maintenance
Marcus Hollern
(555) 287-6419
BrookvalePM382@ [login to view URL]
licensed & Insured
FREE ESTIMATES

Back of Card

Interior & Exterior Repairs
Perscision Grass Cutting
Hedge & Shrub Trimming
Landscape & Hardscape
Weed Removal & Control
Mulch Installation
Gutter Cleaning
Spring & Fall Cleanup
Debris Removal
Power Washing
Topsoil & Stone
Lawn Rolling
Tree Trimming
Snow Plowing

and much more!

```html
<!DOCTYPE html>
<html lang="en">
<head>
<meta charset="utf-8">
<title>Brookvale Property Maintenance – Business Cards</title>
<link href="https://fonts.googleapis.com/css2?family=Lato:wght@400;700;900&display=swap" rel="stylesheet">
<style>
  :root {
    --green: #1f8f3f;
    --green-text: #2a8a3e;
    --grass-light: #a6d86a;
    --grass: #5fb83a;
    --meadow-sky: #e6e59a;
    --meadow-field: #8fbf3a;
    --meadow-deep: #3f8a2a;
    --paper: #ffffff;
    --ink: #3d6b3a;
    --backdrop: #e9ebe6;
  }
  * { box-sizing: border-box; margin: 0; padding: 0; }
  html, body { width: 1200px; height: 928px; overflow: hidden; }
  body {
    background: var(--backdrop);
    font-family: "Lato", sans-serif;
    position: relative;
  }
  .card {
    position: absolute;
    width: 600px;
    height: 343px;
    overflow: hidden;
    box-shadow: 0 8px 24px rgba(0,0,0,0.18);
  }

  /* Back of card */
  .card-back { left: 60px; top: 70px; background: var(--paper); }
  .card-back .grass {
    position: absolute;
    left: 0; right: 0; bottom: 0; height: 190px;
    background: linear-gradient(to bottom, rgba(166,216,106,0) 0%, rgba(166,216,106,0.55) 40%, var(--grass) 100%);
  }
  .service-list {
    position: absolute;
    list-style: none;
    font-size: 17px;
    line-height: 23px;
    color: var(--green-text);
  }
  .service-list li { display: flex; align-items: center; gap: 7px; }
  .service-list li::before {
    content: "";
    width: 0; height: 0;
    border-top: 5px solid transparent;
    border-bottom: 5px solid transparent;
    border-left: 8px solid var(--green);
  }
  .services-main { left: 60px; top: 92px; }
  .services-extra { left: 330px; top: 46px; }
  .more-note {
    position: absolute;
    left: 395px; top: 202px;
    font-size: 17px;
    color: var(--green-text);
  }

  /* Front of card */
  .card-front { left: 560px; top: 520px; background: var(--green); }
  .card-front .meadow {
    position: absolute;
    left: 330px; right: 0; top: 0; bottom: 0;
    background:
      radial-gradient(ellipse at 70% 80%, #d8d83a 0%, rgba(216,216,58,0) 45%),
      linear-gradient(to bottom, var(--meadow-sky) 0%, var(--meadow-field) 45%, var(--meadow-deep) 100%);
  }
  .card-front .panel { position: absolute; inset: 0; }
  .brand {
    position: absolute;
    left: 36px; top: 40px;
    display: flex; align-items: center; gap: 10px;
    font-size: 22px; font-weight: 900;
    line-height: 1.1;
    color: var(--green);
  }
  .brand-dot { flex: none; width: 16px; height: 16px; border-radius: 50%; background: var(--green); }
  .brand-name { max-width: 230px; }
  .service-tag {
    position: absolute;
    background: var(--green);
    color: var(--paper);
    font-size: 13px; font-weight: 900;
    padding: 4px 10px;
    border-radius: 10px;
    letter-spacing: 0.3px;
  }
  .tag-lawn { left: 262px; top: 104px; }
  .tag-snow { left: 248px; top: 136px; }
  .tag-landscape { left: 232px; top: 168px; }
  .person-name {
    position: absolute;
    left: 36px; top: 196px;
    font-size: 22px; font-weight: 900;
    color: var(--green);
    letter-spacing: 0.5px;
  }
  .name-rule {
    position: absolute;
    left: 36px; top: 226px;
    width: 248px; height: 3px;
    background: var(--green);
  }
  .credential {
    position: absolute;
    left: 36px; top: 232px;
    font-size: 17px;
    color: var(--green);
  }
  .contact {
    position: absolute;
    left: 40px;
    display: flex; align-items: center; gap: 10px;
    font-size: 15px;
    color: var(--ink);
  }
  .contact svg { width: 14px; height: 14px; fill: var(--ink); }
  .contact-phone { top: 260px; }
  .contact-email { top: 282px; }
  .estimate-tag {
    position: absolute;
    left: 14px; top: 304px;
    background: var(--green);
    color: var(--paper);
    font-size: 18px; font-weight: 700;
    padding: 3px 16px 3px 18px;
    border-radius: 0 14px 14px 0;
    letter-spacing: 0.5px;
  }
</style>
</head>
<body>

  <section class="card card-back" aria-label="Back of card">
    <div class="grass" role="img" aria-label="Tall green grass along the bottom edge"></div>
    <ul class="service-list services-main">
      <li>Interior &amp; Exterior Repairs</li>
      <li>Perscision Grass Cutting</li>
      <li>Hedge &amp; Shrub Trimming</li>
      <li>Landscape &amp; Hardscape</li>
      <li>Weed Removal &amp; Control</li>
      <li>Mulch Installation</li>
      <li>Gutter Cleaning</li>
      <li>Spring &amp; Fall Cleanup</li>
    </ul>
    <ul class="service-list services-extra">
      <li>Debris Removal</li>
      <li>Power Washing</li>
      <li>Topsoil &amp; Stone</li>
      <li>Lawn Rolling</li>
      <li>Tree Trimming</li>
      <li>Snow Plowing</li>
    </ul>
    <p class="more-note">and much more!</p>
  </section>

  <section class="card card-front" aria-label="Front of card">
    <div class="meadow" role="img" aria-label="Sunny meadow with yellow wildflowers and green fields"></div>
    <svg class="panel" viewBox="0 0 600 343" width="600" height="343" aria-hidden="true">
      <path d="M14 14 H345 C395 90 400 230 470 329 H14 Z" fill="var(--paper)" stroke="var(--green)" stroke-width="8"/>
    </svg>

    <div class="brand"><span class="brand-dot"></span><span class="brand-name">Brookvale Property Maintenance</span></div>

    <span class="service-tag tag-lawn">LAWN CARE</span>
    <span class="service-tag tag-snow">SNOW PLOWING</span>
    <span class="service-tag tag-landscape">LANDSCAPING</span>

    <h1 class="person-name">MARCUS HOLLERN</h1>
    <div class="name-rule"></div>
    <p class="credential">Licensed &amp; Insured</p>

    <p class="contact contact-phone">
      <svg viewBox="0 0 24 24"><path d="M6.6 10.8a15.1 15.1 0 0 0 6.6 6.6l2.2-2.2a1 1 0 0 1 1-.25 11.4 11.4 0 0 0 3.6.57 1 1 0 0 1 1 1V20a1 1 0 0 1-1 1A17 17 0 0 1 3 4a1 1 0 0 1 1-1h3.5a1 1 0 0 1 1 1c0 1.25.2 2.45.57 3.57a1 1 0 0 1-.25 1z"/></svg>
      (555) 287-6419
    </p>
    <p class="contact contact-email">
      <svg viewBox="0 0 24 24"><path d="M2 5h20v14H2z M2 5l10 8 10-8" fill="none" stroke="var(--ink)" stroke-width="2"/></svg>
      BrookvalePM382@inboxmail.net
    </p>

    <p class="estimate-tag">FREE ESTIMATES</p>
  </section>

</body>
</html>
```